Personalised Poetry business needs a business card designed

I am a writer that specialises in personalised poetry for people for significant life events.
I want a business card that stands out and portrays class and professionalism but is also welcoming & indicates warmth and honesty.
I'm happy with the logo that was designed for me, I would like to see it in raised print on the business card. I am open to suggestions on colours but think perhaps gold or silver writing for the logo would look good. I would like just the logo and my name and contact details on the front of the card. On the back of the card, I would like a list of the different events I provide poems for I will upload a photo of my current business card for reference. My current logo has a shading behind it that I don't like, I just want the words of the logo without any background colour

Target Market(s)

People wanting to provide a unique gift to someone special in their life

Industry/Entity Type

Writer

Contact Information for Business Card

Logo, my name and contact details on the front and a list of all the events I write poetry for on the back

Font styles to use
Script

Requirements
Must have
• I would like to see the logo, if possible, in a raised type of print on the card so that you can feel the actual words. I would like to have a glossy finish to the card and be able to print it on good quality board
Should not have
• The shading that is currently behind the logo on my current business card

```html
<!DOCTYPE html>
<html lang="en">
<head>
<meta charset="utf-8">
<title>Lines for Always – Business Card</title>
<link rel="stylesheet" href="https://fonts.googleapis.com/css2?family=Crimson+Text:wght@400&family=Pinyon+Script&family=Questrial&display=swap">
<style>
  :root {
    --backdrop: #ababab;
    --card-dark: #333333;
    --logo-ink: #1c1c1c;
    --tagline-ink: #262626;
    --card-light: #f4f4f4;
    --text-ink: #4a4a4a;
    --shadow: rgba(0, 0, 0, 0.28);
  }
  * { margin: 0; padding: 0; box-sizing: border-box; }
  html, body {
    width: 1200px;
    height: 1000px;
    overflow: hidden;
    background: var(--backdrop);
  }
  .canvas {
    position: relative;
    width: 1200px;
    height: 1000px;
  }
  .card {
    position: absolute;
    left: 293px;
    width: 615px;
    height: 354px;
    box-shadow: 0 2px 4px var(--shadow);
  }
  .card--front {
    top: 132px;
    background: var(--card-dark);
  }
  .card--back {
    top: 530px;
    background: var(--card-light);
    color: var(--text-ink);
  }
  .brand-name {
    position: absolute;
    left: 0;
    width: 100%;
    top: 110px;
    text-align: center;
    font-family: "Crimson Text", Georgia, serif;
    font-size: 64px;
    line-height: 1;
    color: var(--logo-ink);
  }
  .brand-tagline {
    position: absolute;
    left: 0;
    width: 100%;
    top: 196px;
    text-align: center;
    font-family: "Questrial", Arial, sans-serif;
    font-size: 22px;
    letter-spacing: 0.5px;
    color: var(--tagline-ink);
  }
  .back-heading {
    position: absolute;
    left: 0;
    width: 100%;
    top: 44px;
    text-align: center;
    font-family: "Pinyon Script", cursive;
    font-size: 34px;
    line-height: 1.2;
  }
  .event-list {
    position: absolute;
    left: 59px;
    top: 124px;
    list-style: none;
    font-family: "Crimson Text", Georgia, serif;
    font-size: 19px;
    line-height: 30px;
  }
  .event-list li {
    padding-left: 10px;
    text-indent: -10px;
    width: 215px;
  }
  .event-list li::before { content: "• "; }
  .contact {
    position: absolute;
    right: 57px;
    top: 206px;
    text-align: right;
    font-family: "Crimson Text", Georgia, serif;
    font-size: 18px;
    line-height: 22px;
  }
  .contact-name {
    font-family: "Pinyon Script", cursive;
    font-size: 36px;
    line-height: 46px;
  }
</style>
</head>
<body>
<main class="canvas">
  <section class="card card--front" aria-label="Card front">
    <div class="brand-name">Lines for Always</div>
    <div class="brand-tagline">Personalised Poetry</div>
  </section>

  <section class="card card--back" aria-label="Card back">
    <h1 class="back-heading">Momentous Life Events Personalise in Poetry</h1>
    <ul class="event-list">
      <li>Weddings &amp; Anniversaries</li>
      <li>Birthdays &amp; Christmas</li>
      <li>Valentines Day</li>
      <li>Retirements, Business &amp; Corporate Events</li>
      <li>Funerak &amp; Eulogies</li>
    </ul>
    <address class="contact" style="font-style: normal;">
      <div class="contact-name">Marcus Hale</div>
      <div class="contact-phone">0412 555 017</div>
      <div class="contact-email">marcus@linesforalways.com</div>
    </address>
  </section>
</main>
</body>
</html>
```